Business Card - high end, modern health care

Hey designers!

We need a double sided business card for the boutique, cutting edge physical therapy rehabilitation centre in Sydney's Northern Beaches.

With the most qualified physios in the area The Harbourline Motion Clinic does what other physiotherapy practices do not, we take our time with our patients giving them longer appointments, better physios and therefor faster results!

We guarantee that the service people receive at THMC will be unparalleled.

Hence we need a business card to reflect our modern, boutique, high end service. The final design needs to reflect that we are in a class of our own yet with the feel of beachside retreat.

Below I have attached our logo in both blue on white and white on blue. The exact colour is;
and the font that we have used in our logo is Tex Gyre Aventador.

I like the idea of the blue as the main colour as it is more eye catching and our signage onto the main road will be in this blue and in the interest of consistency across marketing the blue needs to be a part of the design. However I would appreciate a few designs onto a wooden background as this is a visual theme within the fitout of the practice.

The design needs to be of standard size (91x55mm).

Target Market(s)

We target people who have an end outcome in mind and those who have had poor experiences with other providers and ensure that everyone gets the care that they deserve with a premium service that is tailored to the individuals circumstances. As a premium service, the target market is highly educated, business and tech savvy with the additional target market of elderly people who have self funded their retirement and see value in paying for the best ongoing rehabilitation to maintain independence.

Industry/Entity Type

Physical Therapy

Contact Information for Business Card

Name, designation( Titled Musculoskeletal Physiotherapist... there will also be those in the company that have multiple designations ie 5 or 6 words long), phone number, email, facebook, instagram, address

Font styles to use
Sans Serif

Colors

Designer to choose colors to be used in the design.

Requirements
Must have
• Front - The logo as large as possible, blue or wooden theme, and all of the important details.
• Back - A blank space/lines on which to write appointment times (no "Appointment, date, time" etc.)
Nice to have
• facebook url
• logos for facebook and instagram
• Mini logos for the phone and email?

```html
<!DOCTYPE html>
<html lang="en">
<head>
<meta charset="utf-8">
<title>The Harbourline Motion Clinic — Appointment Card</title>
<link href="https://fonts.googleapis.com/css2?family=Jost:wght@500;600&display=swap" rel="stylesheet">
<style>
  :root {
    --brand-blue: #0e56a5;
    --card-white: #ffffff;
  }
  html, body {
    margin: 0;
    padding: 0;
    width: 1200px;
    height: 726px;
    overflow: hidden;
    background: var(--brand-blue);
  }
  .appointment-card {
    position: relative;
    width: 1200px;
    height: 726px;
    background: var(--brand-blue);
    color: var(--card-white);
    font-family: "Jost", "Helvetica Neue", Arial, sans-serif;
  }
  .card-heading {
    position: absolute;
    top: 92px;
    left: 0;
    width: 100%;
    margin: 0;
    text-align: center;
    font-size: 76px;
    font-weight: 600;
    letter-spacing: -0.5px;
    line-height: 1;
  }
  .next-appointment-label {
    position: absolute;
    top: 270px;
    left: 39px;
    margin: 0;
    font-size: 50px;
    font-weight: 600;
    line-height: 1;
  }
  .writing-lines {
    position: absolute;
    left: 0;
    top: 0;
  }
</style>
</head>
<body>
  <main class="appointment-card">
    <h1 class="card-heading">Thanks for visiting!</h1>
    <p class="next-appointment-label">Your Next Appointment is:</p>
    <svg class="writing-lines" width="1200" height="726" viewBox="0 0 1200 726" aria-hidden="true">
      <g stroke="var(--card-white)" stroke-width="3.5">
        <line x1="33" y1="429" x2="1168" y2="429"/>
        <line x1="33" y1="503" x2="1168" y2="503"/>
        <line x1="33" y1="576" x2="1168" y2="576"/>
        <line x1="33" y1="650" x2="1168" y2="650"/>
      </g>
    </svg>
  </main>
</body>
</html>
```